Velmora CBD Tincture packaging design

We are seeking a designer to create the label that will be printed on cardboard box packaging, which will carry our CBD tincture. We envision the box being white to resemble a clean look that stands out on shelves. Our logo (attached) uses shades of yellows and greens in the form of a fluid drop resembling half plant and half plant extract. The packaging will show that we only use clean (TRUNK certified) hemp extract thats been extracted using the cleanest method of extraction; supercritical CO2. Our tincture uses a fractionated coconut oil to improve absorption for the consumer, increasing onset time and providing essential omega fatty acids. We take pride in our use of a clean product with a clean extraction. The tincture bottle itself holds 30ml of liquid and is a clear glass bottle. The cap for the tincture bottle is white and has a graduated glass stem that shows the measurements for how much liquid it holds (picture attached). We have not yet done the label that will stick on the tincture, but i image it will be a frosted white label with the Velmora logo and a few words describing the product. This project is for the cardboard box that will hold each individual tincture bottle.

BOX DIMENSIONS: 1.31" x 1.31" x 4.13" (LxWxH)

We will be releasing a new product (cbd capsules) in April, and we will reach out to the designer of this product as first option to create the design for the capsule packaging.

Target Market(s)

convenience stores, medical marijuana dispensaries, health stores

Font styles to use
Serif

Colors
ffffff
fbed22
ffc214
ffcf3e
acd136
9bcb3c

Requirements
Must have
• -Velmora company logo
-Made with full spectrum supercritical CO2 Hemp Extract
-Made from TRUNK certified clean hemp
-Declaration of ingredients (fractionated coconut oil, CBD hemp extract)
-1200mg CBD Tincture
-Nt. Wt. 1FL OZ (30ml)
-These statements have not been evaluated by the Food and Drug Administration. FDA has not evaluated this product for safety or efficacy. This product is not intended to diagnose, treat, cure or prevent any disease.
-DO NOT REFRIGERATE. Keep at room temperature to preserve freshness. Store away from humidity, heat, and light. Warning: If pregnant, nursing or taking prescription drugs, consult your physician prior to use. Keep out of reach of children.
-Manufactured by Velmora CBD Co. 58 Quarry Bend Rd. Scarborough, ME 04019
-Batch ID:___________
-Expiration Date:____________
-Good Manufacturing Practice (GMP) Logo
-TRUNK logo
Nice to have
• -Contains omega 3, 6 and essential fatty acids
-Graduated dropper for precise dosing
-40mg of CBD per dropper!
-Made in the USA
-No Pesticides
-No Solvents
-No Heavy Metals
-CO2 Extraction
-3rd Party Lab Tested

```html
<!DOCTYPE html>
<html lang="en">
<head>
<meta charset="utf-8">
<title>Velmora CBD Tincture – box panels</title>
<link href="https://fonts.googleapis.com/css2?family=Oswald:wght@400;500;600&display=swap" rel="stylesheet">
<style>
  :root {
    --bg: #ffffff;
    --panel: #f3f3f3;
    --panel-edge: #e4e4e4;
    --ink-dark: #1f1f1f;
    --green-deep: #1f8a3c;
    --green-mid: #5fb346;
    --green-light: #9bcb3c;
    --green-pale: #acd136;
    --badge-line: #8fc65a;
    --badge-fill: #edf5e3;
    --usa-red: #d83a3a;
    --usa-blue: #3b4d8f;
  }
  * { box-sizing: border-box; margin: 0; padding: 0; }
  html, body { width: 1200px; height: 1200px; overflow: hidden; background: var(--bg); }
  body { font-family: "Oswald", "Arial Narrow", sans-serif; }

  .canvas { position: relative; width: 1200px; height: 1200px; }

  .panel {
    position: absolute; top: 80px; width: 330px; height: 1040px;
    background: linear-gradient(180deg, #f7f7f7 0%, var(--panel) 100%);
    border: 1px solid var(--panel-edge);
    overflow: hidden;
  }
  .panel--side { left: 270px; }
  .panel--front { left: 600px; }

  .band {
    position: absolute; left: 0; right: 0; bottom: 0; height: 110px;
    background: linear-gradient(180deg, var(--green-pale) 0%, var(--green-mid) 45%, #4aa83e 100%);
    display: flex; align-items: center; justify-content: center;
    color: #ffffff;
  }
  .band--side { background: linear-gradient(180deg, #cfe6b0 0%, var(--green-light) 100%); }
  .band__text { font-size: 28px; font-weight: 400; letter-spacing: 0.2px; white-space: nowrap; }
  .band--side .band__text { font-size: 22px; color: #f4f9ec; }

  /* side panel */
  .features { position: absolute; top: 70px; left: 34px; right: 30px;
    color: var(--green-mid); font-size: 17px; line-height: 1.35; font-weight: 400; list-style: none; }
  .dropper-art { position: absolute; top: 250px; left: 60px; width: 110px; height: 180px;
    background: linear-gradient(135deg, #ececec, #d8d8d8); border-radius: 6px; }

  .badges { position: absolute; top: 470px; left: 40px; width: 250px;
    display: grid; grid-template-columns: 1fr 1fr; row-gap: 16px; justify-items: center; }
  .badge { width: 72px; height: 96px; border: 2px solid var(--badge-line); border-radius: 50%;
    display: flex; flex-direction: column; align-items: center; justify-content: center;
    color: var(--green-mid); text-align: center; line-height: 1.0; }
  .badge__big { font-size: 20px; font-weight: 500; }
  .badge__small { font-size: 11px; }
  .badge--usa { border-color: var(--usa-red); color: var(--usa-blue); }
  .badge--cert { background: var(--badge-fill); }

  /* front panel */
  .brand { position: absolute; top: 250px; left: 0; right: 0;
    display: flex; align-items: center; justify-content: center; gap: 14px; }
  .brand__dot { width: 34px; height: 34px; border-radius: 50%; background: var(--green-light); }
  .brand__name { font-size: 64px; font-weight: 500; color: var(--ink-dark); letter-spacing: 0.5px; }

  .headline { position: absolute; top: 460px; left: 0; right: 0; text-align: center;
    color: var(--green-deep); font-size: 40px; font-weight: 600; line-height: 1.28;
    letter-spacing: -0.5px; white-space: nowrap; }
  .certified { position: absolute; top: 720px; left: 0; right: 0; text-align: center;
    color: var(--green-light); font-size: 25px; line-height: 1.3; }
  .strength { position: absolute; top: 825px; left: 0; right: 0; text-align: center;
    color: var(--green-deep); font-size: 25px; }
</style>
</head>
<body>
<main class="canvas">

  <section class="panel panel--side" aria-label="Side panel">
    <ul class="features">
      <li>-Contains omega 3, 6 and essential fatty acids</li>
      <li>-Graduated dropper for precise dosing</li>
      <li>-40mg of CBD per dropper!</li>
    </ul>
    <div class="dropper-art" role="img" aria-label="Drawing of the graduated glass dropper"></div>

    <div class="badges">
      <div class="badge"><span class="badge__big">NO</span><span class="badge__small">HEAVY<br>METALS</span></div>
      <div class="badge"><span class="badge__big">CO2</span><span class="badge__small">EXTRACTION</span></div>
      <div class="badge"><span class="badge__big">NO</span><span class="badge__small">SOLVENTS</span></div>
      <div class="badge"><span class="badge__big">NO</span><span class="badge__small">PESTICIDES</span></div>
      <div class="badge"><span class="badge__big">100%</span><span class="badge__small">NATURAL</span></div>
      <div class="badge badge--usa"><span class="badge__big">MADE</span><span class="badge__small">IN USA</span></div>
      <div class="badge badge--cert" role="img" aria-label="Good Manufacturing Practice certification badge"></div>
      <div class="badge badge--cert" role="img" aria-label="TRUNK certification badge"></div>
    </div>

    <div class="band band--side"><span class="band__text">3rd Party Lab Tested</span></div>
  </section>

  <section class="panel panel--front" aria-label="Front panel">
    <div class="brand">
      <span class="brand__dot" aria-hidden="true"></span>
      <span class="brand__name">Velmora</span>
    </div>

    <h1 class="headline">MADE WITH<br>FULL SPECTRUM<br>SUPERCRITICAL<br>CO2 HEMP EXTRACT</h1>
    <p class="certified">Made from TRUNK<br>certified clean hemp</p>
    <p class="strength">1200mg CBD Tincture</p>

    <div class="band"><span class="band__text">Nt. Wt. 1FL OZ (30ml)</span></div>
  </section>

</main>
</body>
</html>
```